business card design for a plumbing contractor

i need a double business card for a plumbing business, our initial service is residential Sewer Drain Cleaning.

Target Market(s)

other plumbing Business

Industry/Entity Type

Plumbing

Contact Information for Business Card

www.PipeworksTopNotch.example- 5173829046-

Font styles to use
Serif

Colors
ec1f27
0455a3

```html
<!DOCTYPE html>
<html lang="en">
<head>
<meta charset="utf-8">
<title>Pipeworks Top Notch – Business Card</title>
<link rel="stylesheet" href="https://fonts.googleapis.com/css2?family=Roboto+Condensed:wght@300;400;700&display=swap">
<style>
  :root {
    --backdrop: #d9d6d1;
    --card-base: #ecebe8;
    --card-shade: #dcdad6;
    --brand-red: #c8161e;
    --brand-red-deep: #a50f18;
    --logo-grey: #6b6967;
    --on-red: #ffffff;
    --on-red-soft: #f3d9da;
  }
  html, body {
    margin: 0;
    padding: 0;
    width: 1200px;
    height: 969px;
    overflow: hidden;
    background: var(--backdrop);
  }
  .card {
    position: absolute;
    left: 100px;
    top: 200px;
    width: 1000px;
    height: 568px;
    background: linear-gradient(160deg, var(--card-base), var(--card-shade));
    overflow: hidden;
    font-family: "Roboto Condensed", Arial, sans-serif;
    box-shadow: 0 10px 30px rgba(0,0,0,0.18);
  }
  .card__band {
    position: absolute;
    inset: 0;
    width: 1000px;
    height: 568px;
  }
  .brand-name {
    position: absolute;
    left: 57px;
    top: 96px;
    margin: 0;
    font-weight: 700;
    font-size: 50px;
    line-height: 50px;
    color: var(--logo-grey);
    letter-spacing: 0.5px;
  }
  .info {
    position: absolute;
    right: 40px;
    top: 0;
    text-align: right;
    color: var(--on-red);
  }
  .info__name {
    position: absolute;
    right: 0;
    top: 216px;
    margin: 0;
    font-weight: 400;
    font-size: 33px;
    letter-spacing: 1px;
    white-space: nowrap;
  }
  .info__role {
    position: absolute;
    right: 0;
    top: 260px;
    margin: 0;
    font-weight: 400;
    font-size: 24px;
    letter-spacing: 0.5px;
    white-space: nowrap;
  }
  .contact {
    position: absolute;
    right: 0;
    top: 334px;
    margin: 0;
    padding: 0;
    list-style: none;
    font-weight: 300;
    font-size: 21px;
    line-height: 31px;
    color: var(--on-red-soft);
    white-space: nowrap;
  }
  .services {
    position: absolute;
    right: 0;
    top: 432px;
    margin: 0;
    padding: 0;
    list-style: none;
    font-weight: 300;
    font-size: 24px;
    line-height: 31px;
    color: var(--on-red-soft);
    white-space: nowrap;
  }
  .services li::after {
    content: "";
    display: inline-block;
    width: 8px;
    height: 8px;
    margin-left: 14px;
    border-radius: 50%;
    background: var(--on-red-soft);
    vertical-align: middle;
  }
</style>
</head>
<body>
  <section class="card">
    <svg class="card__band" viewBox="0 0 1000 568" aria-hidden="true">
      <defs>
        <linearGradient id="bandFill" x1="0" y1="0" x2="1" y2="1">
          <stop offset="0" stop-color="var(--brand-red)"/>
          <stop offset="1" stop-color="var(--brand-red-deep)"/>
        </linearGradient>
      </defs>
      <polygon points="693,0 1000,0 1000,568 401,568" fill="url(#bandFill)"/>
    </svg>

    <h1 class="brand-name">Pipeworks<br>Top Notch</h1>

    <div class="info">
      <h2 class="info__name">DANIEL REYES</h2>
      <p class="info__role">CEO/FOUNDER</p>
      <ul class="contact">
        <li>Ph : 5173829046</li>
        <li>Dispatcher@PipeworksTopNotch.example</li>
        <li>www.PipeworksTopNotch.example</li>
      </ul>
      <ul class="services">
        <li>Sewer Drain Cleaning</li>
        <li>Maintenance</li>
        <li>Trenchless Pipe Installs</li>
      </ul>
    </div>
  </section>
</body>
</html>
```